Business Card Design - Law Firm

I need a business card design. I have attached a picture of the law firm's website and logo. The business card design should be consistent with those pictures. There should be a place for the employee name, employee job title, telephone number, facsimile number, address, website url, and email address for each employee.
Industry/Entity Type
Business

```html
<!DOCTYPE html>
<html lang="en">
<head>
<meta charset="utf-8">
<title>Whitcombe Law – Business Cards</title>
<link rel="stylesheet" href="https://fonts.googleapis.com/css2?family=Arimo:wght@400;700&display=swap">
<style>
  :root {
    --page-bg: #e9e6e1;
    --card-white: #ffffff;
    --card-black: #1c1c1c;
    --gold: #b39a4e;
    --gold-light: #d4bc6c;
    --rule-grey: #bdbdbd;
    --text-white: #f2f2f2;
  }
  * { box-sizing: border-box; margin: 0; padding: 0; }
  html, body {
    width: 1200px; height: 821px; overflow: hidden;
    background: var(--page-bg);
    font-family: "Arimo", Arial, sans-serif;
  }
  .sheet {
    width: 1200px; height: 821px;
    display: flex; align-items: center; justify-content: center; gap: 40px;
  }
  .card {
    width: 540px; height: 310px;
    border-radius: 14px; overflow: hidden;
    background: var(--card-white);
    box-shadow: 0 6px 18px rgba(0,0,0,.18);
    display: flex; flex-direction: column;
  }
  .card__brand {
    flex: 1;
    display: flex; align-items: center; justify-content: center; gap: 18px;
  }
  .brand__square {
    width: 42px; height: 42px; background: var(--card-black);
  }
  .brand__name {
    font-family: "Arimo", Arial, sans-serif;
    font-weight: 400; font-size: 34px; color: var(--gold);
    padding: 6px 0 10px 18px;
    border-left: 1px solid var(--rule-grey);
  }
  .card__rule {
    height: 4px;
    background: linear-gradient(90deg, var(--gold), var(--gold-light), var(--gold));
  }
  .card__band {
    background: var(--card-black); color: var(--text-white);
  }
  .card--front .card__brand { flex: 0 0 150px; }
  .card--front .card__band {
    flex: 1; display: flex; justify-content: space-between;
    padding: 18px 26px 22px 26px;
  }
  .person { align-self: flex-end; }
  .person__name { color: var(--gold-light); font-size: 21px; font-weight: 400; }
  .person__title { font-size: 14px; margin-top: 3px; }
  .contact { font-size: 13px; line-height: 1.35; }
  .contact__address { margin-bottom: 10px; }
  .contact__line { display: flex; align-items: center; gap: 8px; margin-top: 3px; }
  .contact__icon { width: 14px; height: 14px; flex: none; }
  .card--back .card__band {
    flex: 0 0 54px; display: flex; align-items: center; justify-content: center;
    font-size: 15px; font-weight: 700;
  }
</style>
</head>
<body>
<main class="sheet">
  <section class="card card--front" aria-label="Business card front">
    <div class="card__brand">
      <span class="brand__square"></span>
      <span class="brand__name">Whitcombe Law</span>
    </div>
    <div class="card__rule"></div>
    <div class="card__band">
      <div class="person">
        <p class="person__name">Daniel Fairbourne</p>
        <p class="person__title">President</p>
      </div>
      <div class="contact">
        <p class="contact__address">48 Larkspur Avenue, Suite 310<br>Easton, Vermont 05471</p>
        <p class="contact__line">
          <svg class="contact__icon" viewBox="0 0 16 16" aria-hidden="true"><path fill="var(--gold)" d="M2 6c0-2 2-3 6-3s6 1 6 3v1h-3V5.5H5V7H2zM4 8h8l1.5 5h-11z"/></svg>
          555.018.4620
        </p>
        <p class="contact__line">
          <svg class="contact__icon" viewBox="0 0 16 16" aria-hidden="true"><rect x="1" y="3" width="14" height="10" fill="var(--gold)"/><path d="M1 3l7 6 7-6" fill="none" stroke="var(--card-black)" stroke-width="1.2"/></svg>
          daniel@whitcombelaw.com
        </p>
        <p class="contact__line">
          <svg class="contact__icon" viewBox="0 0 16 16" aria-hidden="true"><g fill="none" stroke="var(--gold)" stroke-width="1.3"><circle cx="8" cy="8" r="6.5"/><ellipse cx="8" cy="8" rx="3" ry="6.5"/><path d="M1.5 8h13M3 4.5h10M3 11.5h10"/></g></svg>
          www.whitcombelaw.com
        </p>
      </div>
    </div>
  </section>

  <section class="card card--back" aria-label="Business card back">
    <div class="card__brand">
      <span class="brand__square"></span>
      <span class="brand__name">Whitcombe Law</span>
    </div>
    <div class="card__rule"></div>
    <div class="card__band">www.whitcombelaw.com</div>
  </section>
</main>
</body>
</html>
```